World first health care product in tablet form to help save relationships and marriages

The product known as Zentharo is in tablet form 470mg and has 30 to a packet the packet size is approx 11cm in length x 4cm We want to use the color of the image attached for the package and cornflower blue for our name Zentharo. We also need to mention close to our name....... maintaining relationships with increased libido and desire ...... Our tablets are in a tamper-proof blister pack inserted into the package. We do not have a logo as yet, we are thinking of zen in small white letters and then THARO in large letters in cornflower blue or something a bit darker. (The O could also contain a smiley face) We are not that fussed with a logo as yet, maybe down the track if our product works and sells. As of today business in Australia has ground to a halt with this coronavirus and its as bad as you could imagine. Please help us make this new product work with a fabulous packet design.
Target Market(s)
females and males
Industry/Entity Type
Pharmaceutical
Requirements
Must have
- the colors of the images attached and cornflower blue

```html
<!DOCTYPE html>
<html lang="en">
<head>
<meta charset="utf-8">
<title>Zentharo Packet Front</title>
<link href="https://fonts.googleapis.com/css2?family=Josefin+Sans:wght@300;400&display=swap" rel="stylesheet">
<style>
  :root {
    --page-bg: #ffffff;
    --pack-blue: #2ea3d6;
    --pack-blue-deep: #2796c8;
    --brand-blue: #1b5f86;
    --text-white: #ffffff;
  }
  * { margin: 0; padding: 0; box-sizing: border-box; }
  html, body {
    width: 1200px;
    height: 1000px;
    overflow: hidden;
    background: var(--page-bg);
  }
  .canvas {
    position: relative;
    width: 1200px;
    height: 1000px;
    display: flex;
    align-items: center;
    justify-content: center;
  }
  .pack-front {
    position: relative;
    width: 1000px;
    height: 364px;
    background: var(--pack-blue);
    overflow: hidden;
    font-family: "Josefin Sans", sans-serif;
    color: var(--text-white);
  }
  .pack-pattern {
    position: absolute;
    inset: 0;
    background: linear-gradient(135deg, var(--pack-blue) 0%, var(--pack-blue-deep) 100%);
  }
  .pack-dosage {
    position: absolute;
    top: 26px;
    right: 34px;
    font-size: 15px;
    font-weight: 300;
    letter-spacing: 0.06em;
    white-space: nowrap;
  }
  .brand-name {
    position: absolute;
    left: 0;
    right: 0;
    top: 104px;
    text-align: center;
    font-size: 88px;
    font-weight: 400;
    line-height: 1;
    letter-spacing: 0.02em;
    color: var(--brand-blue);
    white-space: nowrap;
  }
  .pack-tagline {
    position: absolute;
    left: 0;
    right: 0;
    top: 226px;
    text-align: center;
    font-size: 19px;
    font-weight: 300;
    letter-spacing: 0.12em;
    text-transform: uppercase;
    white-space: nowrap;
  }
</style>
</head>
<body>
  <main class="canvas">
    <section class="pack-front">
      <div class="pack-pattern" role="img" aria-label="Faint geometric line pattern across the blue packet"></div>
      <p class="pack-dosage">470mg • 30 Tablets</p>
      <h1 class="brand-name">Zentharo</h1>
      <p class="pack-tagline">Maintaining relationships with increased libido and desire</p>
    </section>
  </main>
</body>
</html>
```